Computer Repair Shop needs bold business card

An established computer repair shop with a new owner wants a business card that is his own. Keeping with the tradition of the shop the card should be clever with a bold background colour(s). We want to portray a sense of continuity from the last branding because the only thing that changed is the owner. Reliable services, quality parts, fast, friendly, helpful, affordable are still the same and key to the business philosophy.

Target Market(s)

Personal and business computer owners

Industry/Entity Type

Computer Repair

Contact Information for Business Card

please see the file for address details for the card. Card should read Tomas Varga and owner as well.

Font styles to use
Serif
Sans Serif

Colors
fbed22
ffc214
f78f20
f37122
ffffff

Requirements
Must have
• Bold background colours with a tech influence, clear fonts. I added a copy of a PDF flyer we made quickly in the files. It contains the specific details and the colours and style we prefer. The image is from www.pixelmeadowart.com .... not sure if we should be using it for business so we might need to change that but something along those lines is where to start.
Nice to have
• We don't have a logo yet so the name in text with an awesome background is required for now to get our branding process going in the right direction. A map on the back would be nice can be google copy or drawn but must reference court house and library landmarks. "Absolute Satisfaction Guaranteed"
Should not have
• a boring picture of a computer or laptop

```html
<!DOCTYPE html>
<html lang="en">
<head>
<meta charset="utf-8">
<title>Keystone Computers – Business Card</title>
<link rel="stylesheet" href="https://fonts.googleapis.com/css2?family=Open+Sans:wght@400;600;800&family=Libre+Baskerville&display=swap">
<style>
  :root {
    --yellow: #fbed22;
    --gold: #ffc214;
    --orange: #f78f20;
    --deep-orange: #f37122;
    --ink: #1c1406;
    --stage: #e9e4dc;
  }
  * { box-sizing: border-box; margin: 0; padding: 0; }
  html, body { width: 1200px; height: 892px; overflow: hidden; }
  body {
    background: var(--stage);
    font-family: "Open Sans", sans-serif;
    color: var(--ink);
    position: relative;
  }
  .card {
    position: absolute;
    left: 250px;
    width: 700px;
    height: 400px;
    overflow: hidden;
    box-shadow: 0 6px 18px rgba(0,0,0,.18);
  }
  .card--front { top: 30px; background: linear-gradient(100deg, var(--deep-orange), var(--orange) 45%, var(--gold) 100%); }
  .card--back { top: 462px; background: linear-gradient(120deg, var(--deep-orange) 0%, var(--orange) 30%, var(--gold) 65%, var(--yellow) 100%); }
  .waves { position: absolute; inset: 0; width: 100%; height: 100%; }

  .company-name {
    position: absolute;
    left: 0; right: 0; top: 58px;
    text-align: center;
    font-weight: 800;
    font-size: 58px;
    letter-spacing: 1px;
    text-transform: uppercase;
    color: var(--ink);
  }
  .rule {
    position: absolute;
    left: 0; right: 0; top: 168px;
    height: 1.5px;
    background: var(--ink);
  }
  .owner {
    position: absolute;
    left: 150px; top: 222px;
  }
  .owner__name {
    font-family: "Libre Baskerville", serif;
    font-size: 30px;
    line-height: 1.1;
  }
  .owner__title { font-size: 18px; margin-left: 48px; }
  .divider {
    position: absolute;
    left: 372px; top: 196px;
    width: 1.5px; height: 110px;
    background: var(--ink);
  }
  .contact {
    position: absolute;
    left: 392px; top: 204px;
    list-style: none;
    font-size: 16px;
  }
  .contact li { display: flex; align-items: center; gap: 8px; margin-bottom: 10px; }
  .contact svg { width: 16px; height: 16px; flex: none; }

  .back-mark {
    position: absolute;
    left: 0; right: 0; top: 160px;
    text-align: center;
    font-weight: 800;
    font-size: 72px;
    text-transform: uppercase;
    color: var(--deep-orange);
    opacity: .28;
  }
  .services {
    position: absolute;
    top: 38px;
    list-style: none;
    font-size: 17px;
    text-align: right;
    line-height: 1.58;
  }
  .services li::after { content: " \2731"; font-size: 12px; margin-left: 8px; vertical-align: middle; }
  .services--primary { left: 40px; width: 260px; }
  .services--extended { right: 36px; width: 340px; }
</style>
</head>
<body>
  <section class="card card--front" aria-label="Business card front">
    <svg class="waves" viewBox="0 0 700 400" preserveAspectRatio="none" aria-hidden="true">
      <path d="M0 0 H70 C140 60 10 150 80 230 C130 290 60 350 95 400 H0 Z" fill="var(--gold)" opacity=".85"/>
      <path d="M700 0 H610 C560 60 690 140 620 230 C570 300 650 360 600 400 H700 Z" fill="var(--yellow)" opacity=".75"/>
    </svg>
    <h1 class="company-name">Keystone Computers</h1>
    <div class="rule"></div>
    <div class="owner">
      <p class="owner__name">Tomas Varga</p>
      <p class="owner__title">owner</p>
    </div>
    <div class="divider"></div>
    <ul class="contact">
      <li>
        <svg viewBox="0 0 16 16" aria-hidden="true"><rect width="16" height="16" rx="2" fill="var(--ink)"/><path d="M5 3.5l1.8 2-1 1.2c.6 1.4 1.6 2.4 3 3l1.2-1 2 1.8-1.2 1.6c-3.6-.4-6.8-3.6-7.2-7.2z" fill="var(--gold)"/></svg>
        403-555-0182
      </li>
      <li>
        <svg viewBox="0 0 16 16" aria-hidden="true"><rect width="16" height="16" rx="2" fill="var(--ink)"/><path d="M8 3a3.2 3.2 0 0 0-3.2 3.2C4.8 9 8 13 8 13s3.2-4 3.2-6.8A3.2 3.2 0 0 0 8 3zm0 4.4a1.2 1.2 0 1 1 0-2.4 1.2 1.2 0 0 1 0 2.4z" fill="var(--gold)"/></svg>
        212,5120 47th Avenue Lacombe,AB
      </li>
    </ul>
  </section>

  <section class="card card--back" aria-label="Business card back">
    <p class="back-mark" aria-hidden="true">Keystone Computers</p>
    <ul class="services services--primary">
      <li>Virus Removal</li>
      <li>Data Recovery</li>
      <li>Screen Replacement</li>
      <li>Keyboard Replacement</li>
      <li>Battery Replacement</li>
      <li>Network Set Up</li>
    </ul>
    <ul class="services services--extended">
      <li>Software Installations</li>
      <li>Printer Set Up</li>
      <li>Hard Drive Testing</li>
      <li>Computer Upgrades</li>
      <li>New Computer Set Up</li>
      <li>Custom Builds-Gamer</li>
      <li>Custom Builds-Home or Business</li>
      <li>Computer Concierge Service</li>
      <li>Free Cleaning with every package</li>
    </ul>
  </section>
</body>
</html>
```